Business card design for online Mandarin Learning School

We need a business card design for our online language learning school called "Maple Bridge Online for Mandarin Learning". Our existing website is https://www.maplebridgeonline.com
We have our logo already. We would like to see our business card design that can make our online teaching services to be innovative, young, energetic and fun to learn. Prefer to have a certain level of color matching with our website. Apart from "Maple Bridge Online", need to specifically state "for Mandarin Learning" as well on the business card.

```html
<!DOCTYPE html>
<html lang="en">
<head>
<meta charset="utf-8">
<title>Maple Bridge Online for Mandarin Learning – Business Card</title>
<link href="https://fonts.googleapis.com/css2?family=Montserrat:wght@700&family=Open+Sans:wght@400;600&display=swap" rel="stylesheet">
<style>
  :root {
    --teal: #1ba8b5;
    --red: #e0595a;
    --grey: #818283;
    --ink: #2e2e2e;
    --muted: #6f6f6f;
    --card-front: #ffffff;
    --card-back: #f5f9fa;
    --page: #e9ecee;
  }
  * { margin: 0; padding: 0; box-sizing: border-box; }
  html, body { width: 1200px; height: 1200px; overflow: hidden; background: var(--page); }
  .canvas { position: relative; width: 1200px; height: 1200px; }
  .card {
    position: absolute; left: 120px; width: 960px; height: 546px; overflow: hidden;
    box-shadow: 0 6px 24px rgba(0,0,0,0.12);
    font-family: "Open Sans", Arial, sans-serif;
  }
  .card--front { top: 36px; background: var(--card-front); }
  .card--back { top: 618px; background: var(--card-back); }
  .card__bands { position: absolute; inset: 0; width: 100%; height: 100%; }

  .holder { position: absolute; left: 58px; top: 88px; }
  .holder__name { font-family: "Montserrat", Arial, sans-serif; font-weight: 700; font-size: 40px; color: var(--red); line-height: 1; }
  .holder__name span { font-family: "Open Sans", Arial, sans-serif; font-weight: 400; }
  .holder__role { font-size: 22px; font-weight: 400; color: var(--muted); letter-spacing: 0.5px; margin-top: 2px; }

  .contact { position: absolute; left: 58px; display: flex; align-items: center; gap: 34px; font-size: 19px; color: var(--ink); line-height: 1.2; }
  .contact__icon { width: 60px; height: 60px; flex: none; }
  .contact--phone { top: 200px; }
  .contact--web { top: 266px; }
  .contact--mail { top: 330px; }
  .contact--address { top: 395px; }

  .brand { position: absolute; text-align: center; color: var(--teal); font-weight: 400; line-height: 1.15; text-transform: uppercase; letter-spacing: 0.5px; }
  .brand__dot { display: block; margin: 0 auto 14px; border-radius: 50%; background: var(--teal); }
  .brand--front { left: 400px; top: 40px; width: 420px; font-size: 30px; }
  .brand--front .brand__dot { width: 90px; height: 90px; }
  .brand--back { left: 500px; top: 300px; width: 420px; font-size: 29px; }
  .brand--back .brand__dot { width: 90px; height: 90px; }

  .back-url { position: absolute; left: 460px; top: 68px; display: flex; align-items: center; gap: 8px; font-size: 17px; color: var(--red); letter-spacing: 0.3px; }
  .back-url__mark { width: 24px; height: 24px; border-radius: 50%; background: var(--red); }
</style>
</head>
<body>
<main class="canvas">

  <section class="card card--front" aria-label="Business card front">
    <svg class="card__bands" viewBox="0 0 960 546" preserveAspectRatio="none" aria-hidden="true">
      <polygon fill="var(--grey)" points="960,160 960,546 700,546"/>
      <polygon fill="var(--teal)" points="960,330 960,420 850,546 752,546"/>
    </svg>

    <div class="holder">
      <p class="holder__name">NAME <span>HERE</span></p>
      <p class="holder__role">DESIGNATION</p>
    </div>

    <div class="contact contact--phone">
      <svg class="contact__icon" viewBox="0 0 60 60" aria-hidden="true">
        <circle cx="30" cy="30" r="30" fill="var(--teal)"/>
        <rect x="18" y="16" width="24" height="28" rx="3" fill="none" stroke="#fff" stroke-width="2.5"/>
        <path d="M24 22c-2 3 1 11 8 14l3-3-3-3-2 1c-2-1-3-3-4-5l1-2-3-2z" fill="#fff"/>
      </svg>
      <p>000 000 0000<br>000 000 0000</p>
    </div>

    <div class="contact contact--web">
      <svg class="contact__icon" viewBox="0 0 60 60" aria-hidden="true">
        <circle cx="30" cy="30" r="30" fill="var(--teal)"/>
        <g fill="none" stroke="#fff" stroke-width="2">
          <circle cx="30" cy="30" r="14"/>
          <ellipse cx="30" cy="30" rx="6" ry="14"/>
          <line x1="16" y1="30" x2="44" y2="30"/>
          <line x1="18" y1="23" x2="42" y2="23"/>
          <line x1="18" y1="37" x2="42" y2="37"/>
        </g>
      </svg>
      <p>www.maplebridgeonline.com</p>
    </div>

    <div class="contact contact--mail">
      <svg class="contact__icon" viewBox="0 0 60 60" aria-hidden="true">
        <circle cx="30" cy="30" r="30" fill="var(--teal)"/>
        <rect x="16" y="20" width="28" height="20" fill="#fff"/>
        <polyline points="16,20 30,31 44,20" fill="none" stroke="var(--teal)" stroke-width="2"/>
      </svg>
      <p>hello@maplebridgeonline.com</p>
    </div>

    <div class="contact contact--address">
      <svg class="contact__icon" viewBox="0 0 60 60" aria-hidden="true">
        <circle cx="30" cy="30" r="30" fill="var(--red)"/>
        <path d="M30 14a9 9 0 0 0-9 9c0 7 9 17 9 17s9-10 9-17a9 9 0 0 0-9-9z" fill="none" stroke="#fff" stroke-width="2.5"/>
        <circle cx="30" cy="23" r="3" fill="#fff"/>
        <ellipse cx="30" cy="44" rx="8" ry="2.5" fill="none" stroke="#fff" stroke-width="2"/>
      </svg>
      <p>421, Address line here,<br>Dummy Code, 45871</p>
    </div>

    <div class="brand brand--front">
      <span class="brand__dot"></span>
      <p>Maple Bridge Online</p>
      <p>for Mandarin Learning</p>
    </div>
  </section>

  <section class="card card--back" aria-label="Business card back">
    <svg class="card__bands" viewBox="0 0 960 546" preserveAspectRatio="none" aria-hidden="true">
      <polygon fill="var(--grey)" points="0,0 380,0 0,420"/>
      <polygon fill="var(--teal)" points="0,0 230,0 0,255"/>
    </svg>

    <p class="back-url"><span class="back-url__mark"></span>WWW.MAPLEBRIDGEONLINE.COM</p>

    <div class="brand brand--back">
      <span class="brand__dot"></span>
      <p>Maple Bridge Online</p>
      <p>for Mandarin Learning</p>
    </div>
  </section>

</main>
</body>
</html>
```